Deaths in the gang

Creation of a cover for the book "Un soir de cendre" (Title to be used, not the English one)
Size: 14 x 20.5 cm (vertical; with bleed-off on the top, the right side and the bottom)
Title: “An evening of ashes” (this title has no meaning, it's just an expression)
Author: "Fabrice Delvaune"
Publisher: “Editions Marbrel” (at the bottom of the page).
Key Words:
gangster, escape, hold up, murders, jewels, love, young woman with auburn hair.
Story:
Gilles Ferrand, a very dangerous gangster and unscrupulous murderer, escapes from prison in order to organize a new hold up. Lieutenant Voisin, one of the police officers in charge of the investigation falls in love with Sylvie Mabrot, a lovely prison supervisor who has been held hostage during the escape of Ferrand.
But Voisin realizes that Sylvie doesn't tell him all the truth.
And soon, several members of the gang die in mysterious circumstances…
The unbelievable truth will be revealed tardily.
Target Market(s)
Readers of detective stories
Industry/Entity Type
Book
Look and feel

```html
<!DOCTYPE html>
<html lang="fr">
<head>
<meta charset="utf-8">
<title>Un soir de cendre — Fabrice Delvaune</title>
<link href="https://fonts.googleapis.com/css2?family=Cinzel:wght@400;500&family=Cinzel+Decorative:wght@400;700&display=swap" rel="stylesheet">
<style>
  :root {
    --page: #ffffff;
    --skin-light: #fbe9cf;
    --skin-mid: #eab592;
    --skin-warm: #c8705a;
    --skin-deep: #7b2c33;
    --night: #031a2c;
    --peach: #e6ad8d;
    --ink: #1d2b39;
    --white: #ffffff;
  }
  * { margin: 0; padding: 0; box-sizing: border-box; }
  html, body {
    width: 1200px;
    height: 1200px;
    overflow: hidden;
    background: var(--page);
  }
  .stage {
    position: relative;
    width: 1200px;
    height: 1200px;
  }
  .cover {
    position: absolute;
    left: 259px;
    top: 80px;
    width: 682px;
    height: 999px;
    overflow: hidden;
  }
  .cover-art {
    position: absolute;
    inset: 0;
    background:
      radial-gradient(ellipse 70% 55% at 35% 40%, var(--skin-light) 0%, var(--skin-mid) 60%, transparent 85%),
      linear-gradient(160deg, var(--skin-mid) 0%, var(--skin-warm) 60%, var(--skin-deep) 100%);
  }
  .night-band {
    position: absolute;
    inset: 0;
    width: 100%;
    height: 100%;
  }
  .night-band path { fill: var(--night); }
  .author {
    position: absolute;
    left: 51px;
    top: 36px;
    font-family: "Cinzel", serif;
    font-weight: 400;
    font-size: 40px;
    letter-spacing: 1px;
    color: var(--ink);
    white-space: nowrap;
  }
  .title {
    position: absolute;
    right: 22px;
    top: 492px;
    text-align: center;
    font-family: "Cinzel Decorative", serif;
    font-weight: 700;
    line-height: 1;
  }
  .title span { display: block; }
  .title .big { color: var(--peach); }
  .title .small { color: var(--white); font-size: 60px; line-height: 0.95; }
  .title .line-un { font-size: 150px; line-height: 0.85; }
  .title .line-cendre { font-size: 60px; line-height: 1.05; letter-spacing: -1px; }
  .publisher {
    position: absolute;
    left: 0;
    width: 684px;
    top: 934px;
    text-align: center;
    font-family: "Cinzel", serif;
    font-weight: 400;
    font-size: 30px;
    letter-spacing: 1px;
    color: var(--white);
  }
</style>
</head>
<body>
<div class="stage">
  <div class="cover">
    <div class="cover-art" role="img" aria-label="Illustration en aplats d'une jeune femme aux cheveux auburn, visage en gros plan"></div>
    <svg class="night-band" viewBox="0 0 682 999" preserveAspectRatio="none" aria-hidden="true">
      <path d="M555 0 C520 80 495 150 486 200 C470 300 420 400 399 479 C375 570 352 650 350 728 C346 820 352 920 356 999 L682 999 L682 0 Z"/>
    </svg>
    <p class="author">Fabrice Delvaune</p>
    <h1 class="title">
      <span class="big line-un">UN</span>
      <span class="small">SOIR</span>
      <span class="small">DE</span>
      <span class="big line-cendre">CENDRE</span>
    </h1>
    <p class="publisher">Editions Marbrel</p>
  </div>
</div>
</body>
</html>
```